Header-Bild für Kreditvergleich-Domain
#56 Das Hintergrundbild hat nichts mit Kreditvergleich zu tun
Und bitte die 1. Zeile alle Buchstaben groß schreiben
#49 Bitte mit anderer Schrift, bzw. anderes Logo. Das sieht noch nicht professionell aus
#33 Idee des Headers ist nicht schlecht. Die Frau vermittelt einen zu legeren Umgang mit Krediten.
Der Schriftzug passt leider gar nicht. Er wirkt nicht seriös. "Einfach und sicher sparen" passt nicht so richtig zum Kreditthema.
Kommentar für alle noch vorhandenen Designvorschläge:
Wichtig ist mir, dass das Layout seriös wirkt. Es handelt sich um eine Vergleichsportal für Kredite. Das Layout soll nicht übertrieben, sondern seriös wirken.
Das oder die Bilder müssen eindeutig zu dem Kreditthema passen.
#24 das geht mal gar nicht.... Das Bild sieht absolut billig aus.
#22 Ist immer noch Urlaub und nicht Finanz.
Die eckigen Bilder sehen übrigens besser aus, als das abgerundete Bild.
#19 Die Farbgebung von grün und weiß ist sehr schön. Was nicht passt, ist ein Apfel bei einer Finanzwebseite. Ich dachte hier zuerst an ein Ernährungsportal. Die Farbe gelb des Logos beisst sich etwas mit dem Rest.
Die Grundidee ist aber nicht schlecht.
#18 Bitte andere Farbgebung probieren. So wie die Farbe ist, passt es nicht zum restlichen Layout.
#16: Layout sehr gut gemacht, aber die Bilder müssen seriös wirken und zu Finanzthemen passen.
#7 und #10
diese beiden Header gefallen mir an sich am besten.
Meine Vorstellungen bezüglich der Übergänge sind leider nicht so geworden, wie ich mir das vorgestellt hatte. Deshalb lassen wir Übergänge ab jetzt weg.
#7: Das Logo und die Schrift ist prima. Vielleicht könnte man mal 2-3 andere Hintergrundbilder verwenden. Etwas heller in der Farbe wäre klasse.
#10: Das Logo und die Schrift ist prima, das Bild aber unpassend. Vielleicht könnte man mal 2-3 andere Hintergrundbilder verwenden.
Danke
Die Übergänge sehen irgendwie nicht sehr gut aus. Das geht bestimmt noch besser.
Der Einkaufswagen wirkt nicht sehr seriös
Das Bild gefällt mir schon mal sehr gut.
An paar Anmerkungen dazu:
1. gut ist, dass der kleine Spruch oben links auf bild Nr. 3 nicht mehr dabei ist
2. Der Logo charakter und das Euro zeichen sind prima
3. Wäre mal möglich, die schrift im dem Logo etwas höher zu setzen?
4. Was bei Nr. 7 irgendwie noch fehlt sind die fließendere Übergänge auf der linken und rechten Seite. Der Übergang ist zu hart.

```html
<!DOCTYPE html>
<html lang="de">
<head>
<meta charset="utf-8">
<title>Kreditlinde.com – Ihr Kredit Vergleichsportal</title>
<link rel="stylesheet" href="https://fonts.googleapis.com/css2?family=Arimo:wght@400;700&family=Noto+Sans:wght@400;700&display=swap">
<style>
  :root {
    --green-dark: #6b9a22;
    --green-mid: #8aa862;
    --green-pale: #e5eed7;
    --green-band: #d5e6bc;
    --notice-bg: #dcefbf;
    --notice-border: #9cca5a;
    --head-bg: #f4f5f1;
    --text: #222;
    --text-muted: #444;
    --rule: #d9c8bd;
    --white: #fff;
  }
  * { box-sizing: border-box; margin: 0; padding: 0; }
  html, body { width: 1200px; height: 1200px; overflow: hidden; background: var(--white); }
  body { font-family: "Noto Sans", Verdana, sans-serif; color: var(--text); position: relative; }

  .site-header { position: absolute; left: 0; top: 0; width: 1200px; height: 171px; overflow: hidden; }
  .header-scene {
    position: absolute; inset: 0;
    background: linear-gradient(180deg, #6f9fd6 0%, #a9c8e6 38%, #b6c98a 52%, #7f9a3a 68%, #8a7a2e 82%, #9c4a24 100%);
  }
  .snapshot {
    position: absolute; border: 7px solid var(--white);
    box-shadow: 1px 2px 4px rgba(0,0,0,.35);
  }
  .snapshot--signing { left: 18px; top: 22px; width: 170px; height: 124px; transform: rotate(-5deg);
    background: linear-gradient(135deg, #a0745a, #d9b99a); }
  .snapshot--keys { left: 186px; top: 14px; width: 170px; height: 126px; transform: rotate(-4deg);
    background: linear-gradient(135deg, #c9a46c, #e8dcc6 60%, #9a8f7e); }
  .snapshot--plane { left: 352px; top: 18px; width: 172px; height: 126px; transform: rotate(-2deg);
    background: linear-gradient(180deg, #9fc0e0, #dbe7f2); }
  .brand { position: absolute; right: 26px; top: 28px; text-align: right; color: var(--white); font-family: "Arimo", Arial, sans-serif; }
  .brand__name { font-size: 44px; font-weight: 700; letter-spacing: 1px; line-height: 1; }
  .brand__tagline { font-size: 21px; font-weight: 700; letter-spacing: 1px; margin-top: 8px; }

  .side-nav { position: absolute; left: 0; top: 171px; width: 250px; height: 441px; background: var(--white); border-right: 1px solid #ddd; }
  .nav-group__title { height: 35px; line-height: 35px; padding-left: 16px; background: var(--head-bg); font-weight: 700; font-size: 14px; border-bottom: 1px solid #ddd; }
  .nav-group__item { height: 35px; line-height: 35px; padding-left: 16px; background: var(--green-pale); font-size: 13.5px; color: var(--text-muted); border-bottom: 1px solid var(--white); }
  .nav-group__spacer { height: 28px; background: var(--green-band); border-bottom: 1px solid var(--white); }

  .content { position: absolute; left: 250px; top: 171px; width: 692px; height: 441px; }
  .content__title { position: absolute; top: 7px; width: 100%; text-align: center; font-family: "Arimo", Arial, sans-serif; font-weight: 700; font-size: 24px; color: var(--green-dark); }
  .content__subtitle { position: absolute; top: 50px; width: 100%; text-align: center; font-family: "Arimo", Arial, sans-serif; font-size: 21px; color: var(--green-mid); letter-spacing: .5px; }
  .money-figure { position: absolute; left: 35px; top: 127px; width: 216px; height: 163px; border: 1px solid #999; background: var(--white); padding: 14px; }
  .money-figure__fill { width: 100%; height: 100%; background: linear-gradient(160deg, #d6e8cf, #7fb07a 55%, #4f7d4a); }
  .intro { position: absolute; left: 269px; top: 121px; width: 400px; font-size: 13.5px; line-height: 22px; }
  .notice { position: absolute; left: 35px; top: 326px; width: 621px; height: 72px; background: var(--notice-bg); border: 1px solid var(--notice-border); border-radius: 4px; padding: 5px 12px; font-size: 13.5px; line-height: 21px; }
  .content__rule { position: absolute; left: 35px; top: 435px; width: 621px; border-top: 2px dotted var(--rule); }

  .benefits { position: absolute; left: 942px; top: 171px; width: 258px; height: 441px; background: var(--green-pale); padding: 13px 14px; }
  .benefits__title { font-weight: 700; font-size: 14.5px; color: #444; margin-bottom: 12px; }
  .benefits__list { list-style: none; }
  .benefits__item { position: relative; font-size: 12.5px; line-height: 19px; color: #333; padding-top: 10px; margin-bottom: 19px; }
  .benefits__item svg { position: absolute; left: 2px; top: -6px; }
  .benefits__item span { display: block; text-indent: 30px; }
  .benefits__usage { position: absolute; left: 14px; top: 408px; font-weight: 700; font-size: 14.5px; color: #444; }
</style>
</head>
<body>
  <header class="site-header">
    <div class="header-scene" role="img" aria-label="Sommerwiese mit Mohnblumen unter blauem Himmel"></div>
    <div class="snapshot snapshot--signing" role="img" aria-label="Foto: Unterschrift unter einen Kreditvertrag"></div>
    <div class="snapshot snapshot--keys" role="img" aria-label="Foto: Übergabe eines Autoschlüssels"></div>
    <div class="snapshot snapshot--plane" role="img" aria-label="Foto: Passagierflugzeug am Himmel"></div>
    <div class="brand">
      <div class="brand__name">KREDITLINDE.com</div>
      <div class="brand__tagline">Ihr Kredit vergleichsportal</div>
    </div>
  </header>

  <nav class="side-nav">
    <div class="nav-group">
      <div class="nav-group__title">Ratenkredit</div>
      <div class="nav-group__item">Nordquell Bank</div>
      <div class="nav-group__item">Alvenor Bank</div>
      <div class="nav-group__item">Tesmar Bank</div>
      <div class="nav-group__spacer"></div>
    </div>
    <div class="nav-group">
      <div class="nav-group__title">Kleinkredit</div>
      <div class="nav-group__item">Nordquell Bank</div>
      <div class="nav-group__item">Rovanta Bank</div>
      <div class="nav-group__item">&nbsp;Alvenor Bank</div>
      <div class="nav-group__spacer"></div>
    </div>
    <div class="nav-group">
      <div class="nav-group__title">Autokredit</div>
      <div class="nav-group__item">Alvenor Bank</div>
      <div class="nav-group__item">Nordquell Bank</div>
    </div>
  </nav>

  <main class="content">
    <h1 class="content__title">Kreditlinde.com - Ihr Kredit Vergleichsportal</h1>
    <p class="content__subtitle">- Der unabhängige Kredit Vergleich -</p>
    <div class="money-figure"><div class="money-figure__fill" role="img" aria-label="Gebündelte Euro-Banknoten"></div></div>
    <p class="intro">Sie wollen sich Ihre Wünsche jetzt gleich erfüllen? Ein Kredit mit festem Zins und gleich bleibenden Raten ist oft deutlich günstiger als ein überzogenes Girokonto. Wenn sie Kredite gründlich vergleichen, sparen Sie viel Geld. Finden Sie bei uns attraktive Kredite schnell und einfach online.</p>
    <p class="notice">Profitieren Sie vom Wettbewerb unter den Kreditanbietern, denn Onlinebanken können aufgrund des Verzichts auf teure Filialen sehr günstige Zinsen anbieten. Trotzdem ist ein sehr guter Service per Telefon oder Internet gegeben.</p>
    <div class="content__rule"></div>
  </main>

  <aside class="benefits">
    <h2 class="benefits__title">Ihre Kredit Vorteile</h2>
    <ul class="benefits__list">
      <li class="benefits__item"><svg width="24" height="22" viewBox="0 0 24 22"><path d="M2 12 L9 19 L22 3" fill="none" stroke="#86c23c" stroke-width="4" stroke-linecap="round" stroke-linejoin="round"/></svg><span>Wünsche gleich erfüllen können</span></li>
      <li class="benefits__item"><svg width="24" height="22" viewBox="0 0 24 22"><path d="M2 12 L9 19 L22 3" fill="none" stroke="#86c23c" stroke-width="4" stroke-linecap="round" stroke-linejoin="round"/></svg><span>einfache Finanzierung über das Internet</span></li>
      <li class="benefits__item"><svg width="24" height="22" viewBox="0 0 24 22"><path d="M2 12 L9 19 L22 3" fill="none" stroke="#86c23c" stroke-width="4" stroke-linecap="round" stroke-linejoin="round"/></svg><span>vom Wettbewerb der Banken profitieren</span></li>
      <li class="benefits__item"><svg width="24" height="22" viewBox="0 0 24 22"><path d="M2 12 L9 19 L22 3" fill="none" stroke="#86c23c" stroke-width="4" stroke-linecap="round" stroke-linejoin="round"/></svg><span>günstige Zinsen durch Banken ohne Filialen</span></li>
      <li class="benefits__item"><svg width="24" height="22" viewBox="0 0 24 22"><path d="M2 12 L9 19 L22 3" fill="none" stroke="#86c23c" stroke-width="4" stroke-linecap="round" stroke-linejoin="round"/></svg><span>sicher, schnell, einfach</span></li>
      <li class="benefits__item"><svg width="24" height="22" viewBox="0 0 24 22"><path d="M2 12 L9 19 L22 3" fill="none" stroke="#86c23c" stroke-width="4" stroke-linecap="round" stroke-linejoin="round"/></svg><span>kostenlose Kreditanfrage</span></li>
    </ul>
    <h2 class="benefits__usage">Verwendungsmöglichkeit:</h2>
  </aside>
</body>
</html>
```